Website for solo law firm
Different areas of law
Hi PH
Changes done and updated.
Thanks
SolarPixelCrafter
Changes done and updated. Kindly check.
Star rating please...
Any Feedback?
Area of Service is primarily Personal Injury defense but it will be broaden to Immigration and Commercial law. At this time, the client is only concentrating in Personal Injury.
Hi tlumbrova ,
Please can you provide area of services?
The project has been VEILED. Please, those designers that have not posted, we are eager to see your designs before we start rating.
Thank you,
tlumbrova
Hello PH
Can you make the contest veiled?
Wex

```html
<!DOCTYPE html>
<html lang="en">
<head>
<meta charset="utf-8">
<title>The Law Office of Daniel R. Whitford</title>
<link rel="stylesheet" href="https://fonts.googleapis.com/css2?family=Tinos:wght@400;700&display=swap">
<style>
:root{
  --ink:#0c0c0c;
  --header:#111214;
  --blue:#1f86cf;
  --blue-light:#5fb4ec;
  --blue-dark:#12609e;
  --page:#ffffff;
  --panel-dark:#242424;
  --panel-dark2:#3a3a3a;
  --panel-light:#e3e3e3;
  --text-dark:#1a1a1a;
  --footer:#2c2c2c;
  --footer-bar:#0a0a0a;
  --muted:#c9c9c9;
}
*{margin:0;padding:0;box-sizing:border-box}
html,body{width:1200px;height:901px;overflow:hidden}
body{position:relative;background:var(--page);font-family:"Tinos","Times New Roman",serif;color:var(--text-dark)}

.site-header{position:absolute;left:0;top:0;width:1200px;height:105px;background:linear-gradient(#1b1c1e,var(--header))}
.brand{position:absolute;left:195px;top:18px;width:250px;text-align:center;color:#d8d8d8}
.brand-mark{display:block;width:36px;height:36px;border-radius:50%;background:var(--blue-dark);margin:0 auto 6px}
.brand-name{font-size:19px;letter-spacing:1px;line-height:22px;text-transform:uppercase}
.header-contacts{position:absolute;left:862px;top:4px;list-style:none}
.header-contacts li{display:flex;align-items:center;height:35px;font-size:16px;color:#e4e4e4}
.header-contacts svg{width:24px;height:24px;margin-right:14px;fill:#cfcfcf}

.main-nav{position:absolute;left:0;top:105px;width:1200px;height:46px;background:linear-gradient(var(--blue-light),var(--blue) 55%,var(--blue-dark))}
.main-nav ul{list-style:none;display:flex;position:absolute;left:238px;top:0;height:46px;align-items:center}
.main-nav li{color:#fff;font-size:29px;line-height:46px;padding:0 26px;position:relative}
.main-nav li:first-child{padding-left:24px}
.main-nav li+li::before{content:"";position:absolute;left:0;top:11px;width:2px;height:25px;background:#fff}

.panel{position:absolute;left:238px;width:724px;border-radius:14px;overflow:hidden;box-shadow:0 2px 5px rgba(0,0,0,.35)}
.panel-side{position:absolute;left:0;top:0;width:293px;height:100%;background:linear-gradient(90deg,var(--panel-dark),var(--panel-dark2))}
.panel-tab{position:absolute;left:25px;top:20px;width:265px;height:36px;border-radius:7px;background:linear-gradient(var(--blue-light),var(--blue) 60%,var(--blue-dark));color:#fff;font-size:22px;font-weight:400;line-height:36px;text-align:center}
.welcome{top:153px;height:273px}
.welcome-text{position:absolute;left:26px;top:72px;width:250px;color:#fff;font-size:15.5px;line-height:20.5px;text-align:justify;text-indent:18px}
.welcome-photo{position:absolute;left:293px;top:0;width:431px;height:273px;background:linear-gradient(100deg,#3a1e0c 0%,#7a4219 30%,#c9953f 55%,#efd9a6 75%,#fbf5e6 100%)}
.clients{top:445px;height:275px;background:var(--panel-light)}
.clients-figure{position:absolute;left:94px;top:75px;width:104px;height:106px;border-radius:8px;background:linear-gradient(#5fb3ec,#1f6fb5)}
.clients-text{position:absolute;left:322px;top:23px;width:377px;font-size:15.5px;line-height:19.5px;text-align:justify;text-indent:36px;color:var(--text-dark)}

.site-footer{position:absolute;left:0;top:752px;width:1200px;height:113px;background:linear-gradient(#343434,var(--footer))}
.footer-brand{position:absolute;left:231px;top:16px;width:196px;text-align:center;color:#a9a9a9}
.footer-brand .brand-mark{width:28px;height:28px;background:#6c6c6c;margin-bottom:4px}
.footer-brand .brand-name{font-size:15px;line-height:18px}
.footer-address{position:absolute;left:798px;top:8px;font-size:11.5px;line-height:13px;color:#f0f0f0;font-style:normal}
.footer-address dl{margin-top:6px;display:grid;grid-template-columns:46px auto}
.footer-bar{position:absolute;left:0;top:865px;width:1200px;height:36px;background:var(--footer-bar);text-align:center;color:var(--muted);font-size:11px}
.footer-links{list-style:none;display:flex;justify-content:center;padding-top:4px;color:#e4e4e4;line-height:13px}
.footer-links li+li::before{content:"|";margin:0 4px}
.copyright{margin-top:3px;font-size:10px;line-height:12px;color:#9a9a9a}
</style>
</head>
<body>
<header class="site-header">
  <div class="brand">
    <span class="brand-mark"></span>
    <div class="brand-name">Daniel R. Whitford</div>
  </div>
  <ul class="header-contacts">
    <li><svg viewBox="0 0 24 24"><path d="M6.6 10.8a15 15 0 0 0 6.6 6.6l2.2-2.2c.3-.3.7-.4 1-.2 1.1.4 2.3.6 3.6.6.6 0 1 .4 1 1V20c0 .6-.4 1-1 1A17 17 0 0 1 3 4c0-.6.4-1 1-1h3.5c.6 0 1 .4 1 1 0 1.3.2 2.5.6 3.6.1.3 0 .7-.2 1z"/></svg>1-800-555-0142</li>
    <li><svg viewBox="0 0 24 24"><path d="M6.6 10.8a15 15 0 0 0 6.6 6.6l2.2-2.2c.3-.3.7-.4 1-.2 1.1.4 2.3.6 3.6.6.6 0 1 .4 1 1V20c0 .6-.4 1-1 1A17 17 0 0 1 3 4c0-.6.4-1 1-1h3.5c.6 0 1 .4 1 1 0 1.3.2 2.5.6 3.6.1.3 0 .7-.2 1z"/></svg>(555) 410-2287</li>
    <li><svg viewBox="0 0 24 24"><path d="M6 3h10v5H6zM3 9h18v10H3zM6 16h10v5H6z"/></svg>(555) 410-2290</li>
  </ul>
</header>

<nav class="main-nav">
  <ul>
    <li>About</li>
    <li>Practice Areas</li>
    <li>News</li>
    <li>Contact us</li>
  </ul>
</nav>

<section class="panel welcome">
  <div class="panel-side"></div>
  <h2 class="panel-tab">Welcome!</h2>
  <p class="welcome-text">Lorem ipsum dolor sit amet, consectetur adipisicing elit, sed do eiusmod tempor incididunt ut labore et dolore magna aliqua. Ut enim ad minim veniam, quis nostrud exercitation ullamco laboris nisi ut aliquip ex ea commodo consequat. Duis aute irure dolor in reprehenderit ...</p>
  <div class="welcome-photo" role="img" aria-label="Photo of a judge's wooden gavel resting on its sound block"></div>
</section>

<section class="panel clients">
  <div class="panel-side"></div>
  <h2 class="panel-tab">Clients</h2>
  <div class="clients-figure" role="img" aria-label="Blue illustration of a group of people standing together"></div>
  <p class="clients-text">Lorem ipsum dolor sit amet, consectetur adipiscing elit. Duis ut augue leo. Cras tincidunt quam quis ante elementum gravida. Mauris venenatis vehicula risus at gravida. Nunc ac urna quam, in molestie tortor. Fusce faucibus lacus eu augue ultrices mollis. Vestibulum blandit orci id augue euismod rhoncus. Etiam a nunc eget neque sagittis adipiscing. Donec vel purus ut ipsum vestibulum pellentesque at sed leo. Aliquam laoreet elit dolor. Vestibulum tempus nisl eu nisl iaculis pharetra. Donec imperdiet hendrerit mauris quis scelerisque.</p>
</section>

<footer class="site-footer">
  <div class="footer-brand">
    <span class="brand-mark"></span>
    <div class="brand-name">Daniel R. Whitford</div>
  </div>
  <address class="footer-address">
    820 W. Harbor Avenue<br>Suite #140<br>Lakemont, FL 30000
    <dl>
      <dt>TEL:</dt><dd>1-800-555-0142</dd>
      <dt></dt><dd>(555) 410-2287</dd>
      <dt>FAX:</dt><dd>(555) 410-2290</dd>
      <dt>E-mail:</dt><dd>info@whitfordlawoffice.com</dd>
    </dl>
  </address>
</footer>
<div class="footer-bar">
  <ul class="footer-links">
    <li>Home</li><li>About</li><li>Practice Areas</li><li>News</li><li>Contact us</li>
  </ul>
  <p class="copyright">Copyright © 2013 www.whitfordlawoffice.com</p>
</div>
</body>
</html>
```